Luxury Corporate Wellness Brochure | Calm Tide Tone Soak

We are looking for a graphic designer to create a premium tri-fold (or other folding brochure, open to elevated formats beyond a trifold) brochure (print + digital PDF) for our corporate wellness brand, Calm Tide Tone Soak.
The brochure will be shared with hotel sales managers, conference services teams, destination management companies (DMCs), and corporate meeting planners throughout Southern California.
Our goal is to position Calm Tide as a luxury wellness partner for conferences, executive retreats, incentive travel, and corporate events.
The brochure should introduce our services, including:
Reset Rooms (dedicated wellness spaces during conferences)
Guided Meditation
Breathwork
Yoga (including chair yoga)
Private Floating Sound Bath experiences
Executive retreat wellness programming
This is not a spa brochure or yoga studio flyer. It should feel like a piece created for a luxury hotel brand.
Design Direction
The design should feel elegant, sophisticated, and editorial.
Think:
Velor Resorts
Nine Harbors Meetings
Brill-Ashford Group Sales
Corvane Resorts
Elmgrove Hotels
Avoid common AI-generated design trends such as:
Purple and teal gradients
Lotus flowers
Stacked stones
Watercolor textures
Dreamcatchers
Mandalas
Generic meditation silhouettes
Overused wellness clichés
The design should rely on:
Beautiful typography
Strong photography
Clean layouts
Generous white space
Minimal icons
A luxury hospitality aesthetic
Deliverables
Print-ready tri-fold brochure (CMYK)
Editable source file (Adobe InDesign preferred)
Press-ready PDF
Digital PDF optimized for email
Assets Provided
I will provide:
Brand logo
Professional photography
Brand colors
Copy/content
Contact information
The designer is welcome to recommend layout improvements while maintaining a premium, hospitality-focused aesthetic.
Overall Goal
The finished brochure should be something a luxury resort sales director would confidently hand to a Summit 700 meeting planner. It should communicate professionalism, exclusivity, and the value of incorporating wellness into corporate events while showcasing Calm Tide Tone Soak as a trusted hospitality partner.

```html
<!DOCTYPE html>
<html lang="en">
<head>
<meta charset="utf-8">
<title>Calm Tide Tone Soak – Corporate Wellness Brochure</title>
<link rel="stylesheet" href="https://fonts.googleapis.com/css2?family=Poppins:wght@300;400;500;600&display=swap">
<style>
  :root{
    --navy:#1e3675;
    --navy-deep:#172c63;
    --blue:#2e9ad8;
    --blue-light:#5cb6ec;
    --ink:#1d1d24;
    --rule:#d9dde6;
    --paper:#ffffff;
    --stage:#ececee;
  }
  *{box-sizing:border-box;margin:0;padding:0}
  html,body{width:1136px;height:1200px;overflow:hidden;background:var(--stage);font-family:"Poppins",sans-serif;color:var(--ink)}
  .spread{position:absolute;left:158px;width:820px;height:580px;background:var(--paper);overflow:hidden;box-shadow:0 2px 8px rgba(0,0,0,.12)}
  .spread--outside{top:13px}
  .spread--inside{top:607px}
  .panel{position:absolute;top:0;height:580px;width:410px;overflow:hidden}
  .panel--left{left:0}
  .panel--right{left:410px}
  .abs{position:absolute}
  .photo{position:absolute}
  h2{font-weight:500;line-height:1.08}
  .title-navy{color:var(--navy);font-size:22px}
  .title-blue{color:var(--blue);font-size:22px}
  .body{font-size:11px;line-height:1.33;color:var(--ink)}
  .body p+p{margin-top:10px}
  .badge{background:var(--blue);color:#fff;font-size:12.5px;font-weight:500;padding:3px 11px}
  .checklist{list-style:none;font-size:11.2px}
  .checklist li{display:flex;align-items:center;gap:6px;height:21.3px}
  .checklist svg{flex:none}
  .brand{font-size:17px;font-weight:400;letter-spacing:1px;color:var(--navy);display:flex;align-items:center;gap:6px}
  .brand-dot{width:9px;height:9px;border-radius:50%;background:var(--blue)}
  .contact{font-size:11.2px;line-height:1.4}
  .contact div{display:flex;align-items:center;gap:6px}
  .contact .phone{font-weight:600}
  .region-band{left:0;top:548px;width:410px;height:22px;background:var(--navy-deep);color:#fff;font-size:11.5px;display:flex;align-items:center;justify-content:center}
  .region-band b{color:var(--blue-light);font-weight:500}
  .region-strip{left:0;top:570px;width:142px;height:10px;background:var(--blue)}
  .cover{background:var(--navy)}
  .cover-title{color:var(--blue-light);font-size:33px;font-weight:400;line-height:1}
  .cover-sub{color:#fff;font-size:21px;font-weight:300;margin-top:4px}
  .cover-text{color:#fff;font-size:11px;line-height:1.3;margin-top:14px;width:250px}
  .cover-lower{left:0;top:318px;width:410px;height:262px;background:#fff}
  .cover-bowl{left:6px;top:318px;width:398px;height:152px;border-radius:0 0 199px 199px / 0 0 152px 152px;background:radial-gradient(ellipse at 50% 30%,#47c9e0 0%,#2a6ea0 50%,#1e3675 100%)}
  .feature-row{display:flex;left:125px;top:500px;width:285px;height:80px;background:#fff}
  .feature{flex:1;text-align:center;color:var(--navy);font-size:10.8px;font-weight:500;line-height:1.15;display:flex;flex-direction:column;align-items:center;justify-content:flex-start;padding-top:14px;border-left:1px solid var(--rule)}
  .feature:first-child{border-left:0}
  .feature-icon{width:22px;height:22px;border:2px solid var(--blue);border-radius:50%;margin-bottom:6px}
  .services-bar{left:18px;top:88px;width:60px;height:383px;background:var(--navy);border-radius:5px;display:flex;flex-direction:column;align-items:center;justify-content:space-around;padding:12px 0}
  .services-bar span{width:24px;height:24px;border:2px solid #cfe4f5;border-radius:50%}
  .services{left:95px;top:98px;width:305px;list-style:none}
  .services li{border-bottom:1px solid var(--rule);padding:5px 0 6px}
  .services li:last-child{border-bottom:0}
  .services h3{color:var(--blue);font-size:12.5px;font-weight:500;line-height:1.2}
  .services p{font-size:10.5px;line-height:1.3}
</style>
</head>
<body>

<section class="spread spread--outside">
  <div class="panel panel--left">
    <h2 class="abs title-navy" style="left:18px;top:26px">Designed for Hotels,<br>Resorts &amp; Event Planners</h2>
    <p class="abs body" style="left:18px;top:88px;width:300px">Calm Tide Tone Soak is a fully managed wellness partner, making it easy to add premium wellness programming to your event calendar.</p>

    <div class="photo" role="img" aria-label="Resort pool at sunset with floating mats" style="left:0;top:152px;width:105px;height:185px;background:linear-gradient(180deg,#c23a6a 0%,#5b2d5e 35%,#1d2440 70%,#234f78 100%)"></div>

    <div class="abs badge" style="left:115px;top:166px">What We Provide</div>
    <ul class="abs checklist" style="left:117px;top:196px">
      <li><svg width="13" height="13" viewBox="0 0 13 13"><circle cx="6.5" cy="6.5" r="5.6" fill="none" stroke="#1e3675" stroke-width="1.3"/><path d="M3.8 6.6l2 2 3.6-4" fill="none" stroke="#1e3675" stroke-width="1.6"/></svg>Venue coordination and layout planning</li>
      <li><svg width="13" height="13" viewBox="0 0 13 13"><circle cx="6.5" cy="6.5" r="5.6" fill="none" stroke="#1e3675" stroke-width="1.3"/><path d="M3.8 6.6l2 2 3.6-4" fill="none" stroke="#1e3675" stroke-width="1.6"/></svg>Guest flow and onsite facilitation</li>
      <li><svg width="13" height="13" viewBox="0 0 13 13"><circle cx="6.5" cy="6.5" r="5.6" fill="none" stroke="#1e3675" stroke-width="1.3"/><path d="M3.8 6.6l2 2 3.6-4" fill="none" stroke="#1e3675" stroke-width="1.6"/></svg>Professional sound practitioner</li>
      <li><svg width="13" height="13" viewBox="0 0 13 13"><circle cx="6.5" cy="6.5" r="5.6" fill="none" stroke="#1e3675" stroke-width="1.3"/><path d="M3.8 6.6l2 2 3.6-4" fill="none" stroke="#1e3675" stroke-width="1.6"/></svg>Premium sound and amplification setup</li>
      <li><svg width="13" height="13" viewBox="0 0 13 13"><circle cx="6.5" cy="6.5" r="5.6" fill="none" stroke="#1e3675" stroke-width="1.3"/><path d="M3.8 6.6l2 2 3.6-4" fill="none" stroke="#1e3675" stroke-width="1.6"/></svg>Float systems for pool-based experiences</li>
      <li><svg width="13" height="13" viewBox="0 0 13 13"><circle cx="6.5" cy="6.5" r="5.6" fill="none" stroke="#1e3675" stroke-width="1.3"/><path d="M3.8 6.6l2 2 3.6-4" fill="none" stroke="#1e3675" stroke-width="1.6"/></svg>Complete setup and breakdown</li>
    </ul>

    <div class="abs" style="left:0;top:356px;width:37px;height:122px;background:var(--blue);border-radius:0 5px 5px 0"></div>
    <div class="photo" role="img" aria-label="Evening pool event with floating mats and warm lights" style="left:42px;top:356px;width:168px;height:122px;background:linear-gradient(180deg,#3a2f4a 0%,#2c4a7a 50%,#2fb8d6 100%)"></div>
    <div class="photo" role="img" aria-label="Night view of illuminated pool lined with floats" style="left:215px;top:356px;width:168px;height:122px;background:linear-gradient(180deg,#1b1e2c 0%,#23344f 45%,#36c2de 100%)"></div>

    <div class="abs brand" style="left:18px;top:498px">Calm Tide<span class="brand-dot"></span></div>
    <div class="abs contact" style="left:157px;top:484px">
      <div class="phone"><svg width="10" height="10" viewBox="0 0 10 10"><path d="M2 1l2 2-1 1.3a6 6 0 0 0 2.7 2.7L7 6l2 2-1.2 1.3C4.5 9 1 5.5.8 2.2z" fill="#2e9ad8"/></svg>555.010.0148</div>
      <div><svg width="10" height="10" viewBox="0 0 10 10"><rect x=".5" y="2" width="9" height="6" fill="none" stroke="#2e9ad8"/><path d="M.5 2L5 5.5 9.5 2" fill="none" stroke="#2e9ad8"/></svg>hello@calmtidetonesoak.com</div>
      <div><svg width="10" height="10" viewBox="0 0 10 10"><circle cx="5" cy="5" r="4.3" fill="none" stroke="#2e9ad8"/><path d="M.7 5h8.6M5 .7c2 2.3 2 6.3 0 8.6M5 .7c-2 2.3-2 6.3 0 8.6" fill="none" stroke="#2e9ad8" stroke-width=".8"/></svg>calmtidetonesoak.com</div>
    </div>
    <div class="abs region-band"><b>Greater Dunmere Valley,</b>&nbsp;(Western Desert Region)</div>
    <div class="abs region-strip"></div>
  </div>

  <div class="panel panel--right cover">
    <div class="abs" style="left:18px;top:18px">
      <h1 class="cover-title">Elevated Wellness</h1>
      <div class="cover-sub">for Exceptional Gatherings</div>
      <p class="cover-text">Luxury sound bath and wellness programming for conferences, retreats, incentive travel, and resort events.</p>
    </div>
    <div class="photo" role="img" aria-label="Resort pool at night with palm trees and floating mats" style="left:0;top:158px;width:410px;height:175px;background:linear-gradient(180deg,#20305e 0%,#2a3b55 40%,#1f7b74 80%,#2aa98e 100%)"></div>
    <div class="abs cover-lower"></div>
    <div class="photo cover-bowl" role="img" aria-label="Guests relaxing on floating mats in a lit pool"></div>
    <svg class="abs" style="left:0;top:300px" width="410" height="40" viewBox="0 0 410 40" aria-hidden="true">
      <path d="M0 30 Q110 0 230 22 T410 14 V24 Q320 38 220 32 T0 38 Z" fill="#fff"/>
    </svg>
    <div class="abs" style="left:0;top:330px;width:14px;height:150px;background:var(--blue)"></div>
    <div class="abs brand" style="left:283px;top:234px;color:#fff">Calm Tide<span class="brand-dot" style="background:#fff"></span></div>
    <div class="photo" role="img" aria-label="Practitioner guiding a guest resting on a float" style="left:0;top:480px;width:125px;height:100px;background:linear-gradient(180deg,#c8d2dc 0%,#6d7d92 50%,#1c2a4a 100%)"></div>
    <div class="abs feature-row">
      <div class="feature"><span class="feature-icon"></span>Corporate<br>Wellness</div>
      <div class="feature"><span class="feature-icon"></span>Floating<br>Sound Baths</div>
      <div class="feature"><span class="feature-icon"></span>Executive<br>Retreats</div>
    </div>
  </div>
</section>

<section class="spread spread--inside">
  <div class="panel panel--left">
    <h2 class="abs title-blue" style="left:18px;top:26px">A Luxury Wellness<br>Partner for<br>Corporate Events</h2>
    <div class="abs body" style="left:18px;top:120px;width:215px">
      <p>Calm Tide Tone Soak creates immersive wellness experiences designed to restore, inspire, and elevate groups.</p>
      <p>From private floating sound baths under the stars to land-based wellness sessions, our experiences are thoughtfully designed for luxury resorts, corporate retreats, conferences, and destination events.</p>
      <p>Each program blends sound, stillness, breath, and atmosphere to create a memorable wellness experience your guests will carry with them long after the event ends.</p>
    </div>
    <div class="photo" role="img" aria-label="Singing bowl and candles beside a resort pool" style="left:250px;top:0;width:160px;height:372px;background:linear-gradient(180deg,#3a3f3a 0%,#8a8f8c 35%,#e8e8e6 70%,#f4f2ef 100%)"></div>
    <div class="abs" style="left:285px;top:408px;width:45px;height:55px;background:var(--blue)"></div>
    <div class="photo" role="img" aria-label="Practitioner playing crystal bowls in violet light" style="left:138px;top:397px;width:143px;height:97px;background:linear-gradient(135deg,#e6c4ee 0%,#a65cc4 55%,#5a3080 100%)"></div>
    <div class="photo" role="img" aria-label="Resort grounds at dusk with palms" style="left:0;top:466px;width:134px;height:114px;background:linear-gradient(180deg,#2a3a6a 0%,#1c2440 50%,#2fb0cf 100%)"></div>
    <div class="photo" role="img" aria-label="Night pool with palms and floats" style="left:138px;top:497px;width:143px;height:83px;background:linear-gradient(180deg,#141a2a 0%,#283c5c 50%,#30bcd9 100%)"></div>
    <div class="photo" role="img" aria-label="Lit pool with rows of floating mats" style="left:285px;top:466px;width:125px;height:114px;background:linear-gradient(180deg,#202c48 0%,#2a4f78 50%,#36c3dc 100%)"></div>
  </div>

  <div class="panel panel--right">
    <h2 class="abs title-navy" style="left:18px;top:26px">Signature Wellness<br>Experiences</h2>
    <div class="photo" role="img" aria-label="Sound bath session in a glowing pool at night" style="left:0;top:460px;width:410px;height:120px;background:linear-gradient(180deg,#ffffff 0%,#8e8fb8 30%,#4d4f8c 60%,#1f7fa0 100%)"></div>
    <div class="abs services-bar"><span></span><span></span><span></span><span></span><span></span><span></span></div>
    <ul class="abs services">
      <li><h3>Reset Rooms</h3><p>Dedicated wellness spaces for conferences, meetings, and multi-day events.</p></li>
      <li><h3>Guided Meditation</h3><p>Calming sessions designed to support focus, presence, and mental clarity.</p></li>
      <li><h3>Breathwork</h3><p>Simple, guided techniques to help guests reset, release stress, and reconnect.</p></li>
      <li><h3>Yoga &amp; Chair Yoga</h3><p>Accessible movement sessions for groups, meetings, and retreat settings.</p></li>
      <li><h3>Private Floating Sound Baths</h3><p>A signature pool-based experience featuring crystal singing bowls, gentle water immersion, and a serene desert atmosphere.</p></li>
      <li><h3>Executive Retreat Programming</h3><p>Custom wellness moments for leadership teams, incentive groups, and high-level corporate gatherings.</p></li>
    </ul>
  </div>
</section>

</body>
</html>
```